b2c portal. ZippyGrub. Attract diners and drinkers to restaurant/bar deals

aggregator site for restaurants and bars to promote their deals/discounts

1. we are an aggregator portal that lists all deals and discounts (Happy Hour, etc.) for restaurants and bars. the layout is similar to Kivo and RoamScout, without the ratings.
2. the target market is identical to Kivo and those searching for restaurants on RoamScout.
3. I have attached a file of a preliminary screenshot of a home page.

Target Market(s)

all guests of restaurants and bars

Number of Pages Required

4 page

Requirements
Must have
• a good story loop.
see Kivo, RoamScout, DashMeals
Should not have
• keep it simple

```html
<!DOCTYPE html>
<html lang="en">
<head>
<meta charset="utf-8">
<title>ZippyGrub – Find Restaurant Offers</title>
<link href="https://fonts.googleapis.com/css2?family=Roboto:wght@300;400;500;700&display=swap" rel="stylesheet">
<style>
:root{
  --orange:#c4521e;
  --teal:#2e6b6b;
  --teal-dark:#285f5f;
  --blush:#f5f1f1;
  --ink:#1e1e1e;
  --muted:#555;
  --footer:#2a2a2a;
  --white:#fff;
}
*{box-sizing:border-box;margin:0;padding:0}
html,body{width:1200px;height:3202px;overflow:hidden}
body{font-family:'Roboto',sans-serif;color:var(--ink);background:var(--white);position:relative}
svg{display:block}

/* header */
.site-header{position:absolute;top:0;left:0;width:1200px;height:77px;background:var(--white)}
.brand{position:absolute;left:101px;top:22px;width:190px;height:38px;background:#f6f4f2;display:flex;align-items:center;justify-content:center;font-size:30px;font-weight:500;color:var(--orange);letter-spacing:.5px}
.main-nav{position:absolute;left:341px;top:32px;display:flex;gap:36px;font-size:13px;font-weight:500}
.main-nav .active{color:var(--orange);text-decoration:underline}
.btn-outline{position:absolute;top:25px;height:29px;border:1.5px solid var(--orange);color:var(--orange);font-size:13px;font-weight:500;display:flex;align-items:center;justify-content:center}
.btn-solid{position:absolute;top:25px;height:29px;background:var(--orange);color:#fff;font-size:13px;font-weight:500;display:flex;align-items:center;justify-content:center}
.lang{position:absolute;left:999px;top:25px;width:70px;height:29px;border:1px solid #999;font-size:11px;display:flex;align-items:center;justify-content:center;gap:6px}
.lang .flag{width:12px;height:8px;background:#3a4a8a}

/* hero */
.hero{position:absolute;top:77px;left:0;width:1200px;height:587px;background:var(--teal)}
.hero-art{position:absolute;top:0;height:587px}
.hero h1{position:absolute;top:100px;width:1200px;text-align:center;color:#fff;font-size:33px;font-weight:700;letter-spacing:.5px}
.search{position:absolute;left:225px;top:179px;width:750px;height:55px;background:#fff;display:flex}
.search .field{flex:1;display:flex;align-items:center;gap:10px;padding-left:18px;font-size:12.5px;color:#333}
.search .field+.field{border-left:1px solid #ccc}
.search .find{width:102px;background:var(--orange);color:#fff;font-weight:700;font-size:17px;display:flex;align-items:center;justify-content:center;gap:6px;border:2px solid #fff;outline:1px solid var(--orange)}
.categories{position:absolute;top:295px;left:217px;display:flex}
.cat{display:flex;flex-direction:column;align-items:center;gap:14px;color:#fff;font-size:13.5px;padding:4px 20px;border-right:1px solid rgba(255,255,255,.25);height:93px}
.cat:last-child{border-right:none}
.tagline{position:absolute;left:341px;top:461px;width:517px;height:50px;border:1.5px solid #8fbcb8;color:#fff;font-size:22px;font-weight:300;display:flex;align-items:center;justify-content:center;letter-spacing:.3px}

/* section titles */
.section-title{position:absolute;width:1200px;text-align:center;font-size:24px;font-weight:500;display:flex;justify-content:center;align-items:center;gap:14px}
.section-title::before,.section-title::after{content:"";width:22px;height:2px;background:var(--orange)}
.on-teal{color:#fff}
.on-teal::before,.on-teal::after{background:#fff}

/* best food */
.best-food{position:absolute;top:664px;left:0;width:1200px;height:409px;background:var(--blush)}
.food-card{position:absolute;top:112px;width:183px}
.food-card .photo{height:200px}
.food-card h3{font-size:11.5px;font-weight:500;margin-top:15px}
.food-card p{font-size:10.5px;color:var(--muted);margin-top:3px}

/* restaurants */
.restaurants{position:absolute;top:1073px;left:0;width:1200px;height:637px;background:#fff}
.city-tabs{position:absolute;top:104px;width:1200px;display:flex;justify-content:center;gap:27px;font-size:11.5px;font-weight:500;color:var(--ink)}
.venue{position:absolute;top:163px;width:300px;height:353px;background:#fff;box-shadow:0 2px 8px rgba(0,0,0,.15)}
.venue .photo{height:200px}
.venue .body{padding:18px 21px}
.stars{display:flex;gap:2px}
.venue h3{font-size:11.5px;font-weight:500;margin-top:10px}
.venue .addr{display:flex;align-items:center;gap:6px;font-size:11px;margin-top:8px}
.venue hr{border:none;border-top:1px solid #ddd;margin:12px -8px 14px 0}
.venue p{font-size:11px;color:#444;line-height:1.4;max-width:218px}
.arrow{position:absolute}
.btn-view{position:absolute;left:499px;top:558px;width:202px;height:35px;border:1.5px solid var(--orange);color:var(--orange);font-size:12.5px;font-weight:500;display:flex;align-items:center;justify-content:center}

/* reviews */
.reviews{position:absolute;top:1710px;left:0;width:1200px;height:362px;background:var(--teal-dark)}
.review{position:absolute;top:113px;width:302px;height:146px;background:#fff;border-radius:4px;padding:26px 24px 0 35px}
.review .quote-open{position:absolute;left:12px;top:6px;font-size:28px;font-weight:700;color:#333;font-family:Georgia,serif}
.review .quote-close{position:absolute;left:197px;top:108px;font-size:28px;font-weight:700;color:#333;font-family:Georgia,serif}
.review p{font-size:11.5px;line-height:1.38;color:#333}
.review .stars{margin-top:7px}
.reviewer{position:absolute;top:280px;display:flex;align-items:center;gap:10px;color:#fff}
.reviewer .avatar{width:30px;height:30px;border-radius:50%;background:#c99a7e}
.reviewer b{font-size:11.5px;font-weight:700;display:block}
.reviewer span{font-size:10px}

/* food near me */
.near{position:absolute;top:2072px;left:0;width:1200px;height:391px;background:var(--blush)}
.near-card{position:absolute;top:115px;width:226px;height:222px;background:#fff}
.near-card .photo{height:174px}
.near-card h3{font-size:13.5px;font-weight:500;text-align:center;margin-top:15px}

/* articles */
.articles{position:absolute;top:2463px;left:0;width:1200px;height:388px;background:#fff}
.article{position:absolute;top:112px;width:462px;height:222px;border:1.5px solid #ccc;display:flex}
.article .photo{flex:none;width:210px;height:100%}
.article .body{flex:none;width:249px;padding:25px 30px 0 37px}
.article time{font-size:10.5px;display:block}
.article h3{font-size:14px;font-weight:500;line-height:1.25;margin-top:9px;max-width:180px}
.article p{font-size:11.5px;line-height:1.4;color:#333;margin-top:12px;max-width:172px}
.article .more{display:inline-block;margin-top:16px;background:var(--orange);color:#fff;font-size:9.5px;font-weight:700;padding:6px 7px}

/* footer */
.site-footer{position:absolute;top:2851px;left:0;width:1200px;height:351px;background:var(--footer);color:#ddd}
.footer-brand{position:absolute;left:150px;top:120px;font-size:50px;font-weight:500;color:var(--orange);letter-spacing:2px}
.footer-col{position:absolute;top:57px}
.footer-col h4{font-size:12.5px;font-weight:700;color:#fff;margin-bottom:22px}
.footer-col ul{list-style:none;font-size:11.5px;line-height:20px}
.contact-item{display:flex;align-items:center;gap:10px;font-size:11.5px;line-height:16px;margin-bottom:18px}
.contact-item .dot{width:24px;height:24px;border-radius:50%;background:#fff;display:flex;align-items:center;justify-content:center;flex:none}
.footer-rule{position:absolute;left:122px;top:269px;width:950px;border-top:1px solid #444}
.copyright{position:absolute;top:313px;left:505px;font-size:9.5px}
</style>
</head>
<body>

<header class="site-header">
  <div class="brand">ZippyGrub</div>
  <nav class="main-nav">
    <span class="active">HOME</span><span>FOOD</span><span>RESTAURANTS</span><span>HOW IT WORKS</span><span>BLOG</span>
  </nav>
  <div class="btn-outline" style="left:822px;width:78px">SIGN IN</div>
  <div class="btn-solid" style="left:909px;width:79px">JOIN US</div>
  <div class="lang"><span class="flag"></span>EN<svg width="8" height="5"><path d="M0 0h8L4 5z" fill="#333"/></svg></div>
</header>

<section class="hero">
  <div class="hero-art" role="img" aria-label="Illustrated fast food border: fries, pizza, tomato, chicken leg, burger, popcorn" style="left:0;width:300px;background:linear-gradient(90deg,rgba(232,150,50,.55),rgba(46,107,107,0))"></div>
  <div class="hero-art" role="img" aria-label="Illustrated fast food border: hot dogs, nuggets, olives, soda cup, sandwich" style="right:0;width:300px;background:linear-gradient(270deg,rgba(232,150,50,.55),rgba(46,107,107,0))"></div>
  <h1>FIND RESTAURANT OFFERS</h1>
  <div class="search">
    <div class="field"><svg width="10" height="14" viewBox="0 0 10 14"><path d="M5 0a5 5 0 0 0-5 5c0 4 5 9 5 9s5-5 5-9a5 5 0 0 0-5-5zm0 7a2 2 0 1 1 0-4 2 2 0 0 1 0 4z" fill="#333"/></svg>RESTAURANT LOCATIONS</div>
    <div class="field"><svg width="16" height="14" viewBox="0 0 16 14"><rect x="1" y="4" width="14" height="9" fill="none" stroke="#333" stroke-width="1.3"/><path d="M1 4l2-3h10l2 3" fill="none" stroke="#333" stroke-width="1.3"/><rect x="5" y="7" width="6" height="6" fill="none" stroke="#333"/></svg>RESTAURANT / BAR NAME</div>
    <div class="find"><svg width="13" height="13" viewBox="0 0 13 13"><circle cx="5.5" cy="5.5" r="4" fill="none" stroke="#fff" stroke-width="2"/><path d="M8.5 8.5l3.5 3.5" stroke="#fff" stroke-width="2"/></svg>FIND</div>
  </div>
  <div class="categories">
    <div class="cat"><svg width="42" height="42" viewBox="0 0 42 42"><circle cx="21" cy="21" r="18" fill="none" stroke="#fff" stroke-width="3"/><path d="M21 10v11l7 5" fill="none" stroke="#fff" stroke-width="3"/></svg>Happy Hour</div>
    <div class="cat"><svg width="42" height="42" viewBox="0 0 42 42"><circle cx="11" cy="11" r="6" fill="none" stroke="#fff" stroke-width="3"/><circle cx="31" cy="31" r="6" fill="none" stroke="#fff" stroke-width="3"/><path d="M34 5L8 37" stroke="#fff" stroke-width="3"/></svg>Daily Deals / Discounts</div>
    <div class="cat"><svg width="42" height="42" viewBox="0 0 42 42"><rect x="4" y="7" width="34" height="32" fill="none" stroke="#fff" stroke-width="2.5"/><path d="M4 15h34M12 3v8M30 3v8" stroke="#fff" stroke-width="2.5"/><g fill="#fff"><rect x="10" y="20" width="4" height="4"/><rect x="19" y="20" width="4" height="4"/><rect x="28" y="20" width="4" height="4"/><rect x="10" y="29" width="4" height="4"/><rect x="19" y="29" width="4" height="4"/><rect x="28" y="29" width="4" height="4"/></g></svg>Special Events</div>
    <div class="cat"><svg width="48" height="42" viewBox="0 0 48 42"><path d="M2 8h28v22H2zM30 16h9l7 8v6H30" fill="none" stroke="#fff" stroke-width="2"/><circle cx="10" cy="33" r="4" fill="var(--teal)" stroke="#fff" stroke-width="2"/><circle cx="38" cy="33" r="4" fill="var(--teal)" stroke="#fff" stroke-width="2"/></svg>Delivery/Takeout</div>
    <div class="cat"><svg width="46" height="42" viewBox="0 0 46 42"><path d="M3 9h40v7a5 5 0 0 0 0 10v7H3v-7a5 5 0 0 0 0-10z" fill="none" stroke="#fff" stroke-width="2"/><path d="M17 11v20" stroke="#fff" stroke-dasharray="2 2"/><text x="22" y="26" fill="#fff" font-size="14" font-family="Roboto,sans-serif">%</text></svg>Discount</div>
    <div class="cat"><svg width="40" height="42" viewBox="0 0 40 42"><path d="M3 10h34M3 21h34M3 32h34" stroke="#fff" stroke-width="2.5"/></svg>More</div>
  </div>
  <div class="tagline">YOUR ADVENTURE WITH AFFORDABLE TASTE</div>
</section>

<section class="best-food">
  <h2 class="section-title" style="top:45px">BEST FOOD ITEMS</h2>
  <div class="food-card" style="left:116px"><div class="photo" role="img" aria-label="Spaghetti with tomato sauce on a dark plate" style="background:linear-gradient(135deg,#1f1f1f,#8a3a1c 60%,#222)"></div><h3>LOREM IPSUM</h3><p>Lorem Ipsum is simply dummy</p></div>
  <div class="food-card" style="left:314px"><div class="photo" role="img" aria-label="Grilled chicken salad bowl" style="background:linear-gradient(135deg,#d8d4cc,#6c9a3c 55%,#e6c79a)"></div><h3>LOREM IPSUM</h3><p>Lorem Ipsum is simply dummy</p></div>
  <div class="food-card" style="left:512px"><div class="photo" role="img" aria-label="Cheeseburger on a wooden board" style="background:linear-gradient(180deg,#2a2a2a,#b8692a 55%,#4a2a18)"></div><h3>LOREM IPSUM</h3><p>Lorem Ipsum is simply dummy</p></div>
  <div class="food-card" style="left:708px"><div class="photo" role="img" aria-label="Beef tacos with fresh vegetables" style="background:linear-gradient(135deg,#2b2f33,#7a5a3a 50%,#5a7a3a)"></div><h3>LOREM IPSUM</h3><p>Lorem Ipsum is simply dummy</p></div>
  <div class="food-card" style="left:901px"><div class="photo" role="img" aria-label="Kebab skewers with herbs and onion" style="background:linear-gradient(135deg,#e6e2dc,#7a3a22 50%,#5a8a3a)"></div><h3>LOREM IPSUM</h3><p>Lorem Ipsum is simply dummy</p></div>
</section>

<section class="restaurants">
  <h2 class="section-title" style="top:37px">RESTAURANTS</h2>
  <div class="city-tabs"><span>NEW YORK</span><span>SAN JOSE</span><span>LOS ANGELES</span><span>CHICAGO</span><span>PALO ALTO</span><span>OAKLAND</span><span>MORE CITIES</span></div>
  <svg class="arrow" style="left:70px;top:350px" width="14" height="26"><path d="M12 1L2 13l10 12" fill="none" stroke="#bbb" stroke-width="2"/></svg>
  <svg class="arrow" style="left:1114px;top:350px" width="14" height="26"><path d="M2 1l10 12L2 25" fill="none" stroke="#bbb" stroke-width="2"/></svg>

  <article class="venue" style="left:130px"><div class="photo" role="img" aria-label="Warm-lit restaurant interior with wooden tables" style="background:linear-gradient(180deg,#3a2a1c,#a0703a 60%,#2a1f16)"></div>
    <div class="body"><div class="stars"><svg width="80" height="12"><g fill="none" stroke="var(--orange)" stroke-width="2"><circle cx="6" cy="6" r="4.5"/><circle cx="22" cy="6" r="4.5"/><circle cx="38" cy="6" r="4.5"/><circle cx="54" cy="6" r="4.5"/><circle cx="70" cy="6" r="4.5"/></g></svg></div>
    <h3>LOREM IPSUM IS SIMPLY DUMMY</h3><div class="addr"><svg width="8" height="11" viewBox="0 0 10 14"><path d="M5 0a5 5 0 0 0-5 5c0 4 5 9 5 9s5-5 5-9a5 5 0 0 0-5-5zm0 7a2 2 0 1 1 0-4 2 2 0 0 1 0 4z" fill="#333"/></svg>2210 Maple Row</div><hr>
    <p>Lorem Ipsum is simply dummy text of the printing and typesetting industry</p></div></article>

  <article class="venue" style="left:450px"><div class="photo" role="img" aria-label="Dining room with large windows and a tree at night" style="background:linear-gradient(180deg,#1c2a44,#4a5a4a 60%,#3a2a22)"></div>
    <div class="body"><div class="stars"><svg width="80" height="12"><g fill="none" stroke="var(--orange)" stroke-width="2"><circle cx="6" cy="6" r="4.5"/><circle cx="22" cy="6" r="4.5"/><circle cx="38" cy="6" r="4.5"/><circle cx="54" cy="6" r="4.5"/><circle cx="70" cy="6" r="4.5"/></g></svg></div>
    <h3>LOREM IPSUM IS SIMPLY DUMMY</h3><div class="addr"><svg width="8" height="11" viewBox="0 0 10 14"><path d="M5 0a5 5 0 0 0-5 5c0 4 5 9 5 9s5-5 5-9a5 5 0 0 0-5-5zm0 7a2 2 0 1 1 0-4 2 2 0 0 1 0 4z" fill="#333"/></svg>2210 Maple Row</div><hr>
    <p>Lorem Ipsum is simply dummy text of the printing and typesetting industry</p></div></article>

  <article class="venue" style="left:770px"><div class="photo" role="img" aria-label="Restaurant with wooden booths and pendant lights" style="background:linear-gradient(180deg,#2a2420,#8a5a30 55%,#3a2a1e)"></div>
    <div class="body"><div class="stars"><svg width="80" height="12"><g fill="none" stroke="var(--orange)" stroke-width="2"><circle cx="6" cy="6" r="4.5"/><circle cx="22" cy="6" r="4.5"/><circle cx="38" cy="6" r="4.5"/><circle cx="54" cy="6" r="4.5"/><circle cx="70" cy="6" r="4.5"/></g></svg></div>
    <h3>LOREM IPSUM IS SIMPLY DUMMY</h3><div class="addr"><svg width="8" height="11" viewBox="0 0 10 14"><path d="M5 0a5 5 0 0 0-5 5c0 4 5 9 5 9s5-5 5-9a5 5 0 0 0-5-5zm0 7a2 2 0 1 1 0-4 2 2 0 0 1 0 4z" fill="#333"/></svg>2210 Maple Row</div><hr>
    <p>Lorem Ipsum is simply dummy text of the printing and typesetting industry</p></div></article>

  <div class="btn-view">VIEW MORE RESTAURANTS</div>
</section>

<section class="reviews">
  <h2 class="section-title on-teal" style="top:37px">REVIEWS</h2>
  <svg class="arrow" style="left:94px;top:177px" width="10" height="18"><path d="M9 1L1 9l8 8" fill="none" stroke="#fff" stroke-width="2"/></svg>
  <svg class="arrow" style="left:1094px;top:177px" width="10" height="18"><path d="M1 1l8 8-8 8" fill="none" stroke="#fff" stroke-width="2"/></svg>

  <div class="review" style="left:131px"><span class="quote-open">“</span><p>There are many variations of passages of Lorem Ipsum available, but the majority have suffered alteration in some form, by injected humour, or randomised words which don't look even slightly believable.</p><div class="stars"><svg width="68" height="11"><g fill="none" stroke="var(--orange)" stroke-width="1.8"><circle cx="5.5" cy="5.5" r="4"/><circle cx="19" cy="5.5" r="4"/><circle cx="32.5" cy="5.5" r="4"/><circle cx="46" cy="5.5" r="4"/><circle cx="59.5" cy="5.5" r="4"/></g></svg></div><span class="quote-close">”</span></div>
  <div class="review" style="left:449px"><span class="quote-open">“</span><p>There are many variations of passages of Lorem Ipsum available, but the majority have suffered alteration in some form, by injected humour, or randomised words which don't look even slightly believable.</p><div class="stars"><svg width="68" height="11"><g fill="none" stroke="var(--orange)" stroke-width="1.8"><circle cx="5.5" cy="5.5" r="4"/><circle cx="19" cy="5.5" r="4"/><circle cx="32.5" cy="5.5" r="4"/><circle cx="46" cy="5.5" r="4"/><circle cx="59.5" cy="5.5" r="4"/></g></svg></div><span class="quote-close">”</span></div>
  <div class="review" style="left:766px"><span class="quote-open">“</span><p>There are many variations of passages of Lorem Ipsum available, but the majority have suffered alteration in some form, by injected humour, or randomised words which don't look even slightly believable.</p><div class="stars"><svg width="68" height="11"><g fill="none" stroke="var(--orange)" stroke-width="1.8"><circle cx="5.5" cy="5.5" r="4"/><circle cx="19" cy="5.5" r="4"/><circle cx="32.5" cy="5.5" r="4"/><circle cx="46" cy="5.5" r="4"/><circle cx="59.5" cy="5.5" r="4"/></g></svg></div><span class="quote-close">”</span></div>

  <div class="reviewer" style="left:155px"><div class="avatar" role="img" aria-label="Reviewer portrait"></div><div><b>RICHARD</b><span>Australia</span></div></div>
  <div class="reviewer" style="left:473px"><div class="avatar" role="img" aria-label="Reviewer portrait"></div><div><b>RICHARD</b><span>Australia</span></div></div>
  <div class="reviewer" style="left:790px"><div class="avatar" role="img" aria-label="Reviewer portrait"></div><div><b>RICHARD</b><span>Australia</span></div></div>
</section>

<section class="near">
  <h2 class="section-title" style="top:45px">FOOD NEAR ME</h2>
  <div class="near-card" style="left:131px"><div class="photo" role="img" aria-label="Chicken curry with herbs in a pan" style="background:linear-gradient(135deg,#d9822e,#c0561e 55%,#3a7a2a)"></div><h3>LOREM IPSUM</h3></div>
  <div class="near-card" style="left:368px"><div class="photo" role="img" aria-label="Roast chicken with potatoes" style="background:linear-gradient(135deg,#2a2624,#b0742e 55%,#3a2a20)"></div><h3>LOREM IPSUM</h3></div>
  <div class="near-card" style="left:604px"><div class="photo" role="img" aria-label="Spaghetti on a dark plate" style="background:linear-gradient(135deg,#1f1f1f,#8a3a1c 55%,#222)"></div><h3>LOREM IPSUM</h3></div>
  <div class="near-card" style="left:842px"><div class="photo" role="img" aria-label="Green salad with cheese and pear" style="background:linear-gradient(135deg,#3a3f3f,#4a7a2a 50%,#d8c8a0)"></div><h3>LOREM IPSUM</h3></div>
</section>

<section class="articles">
  <h2 class="section-title" style="top:48px">RECENT ARTICLES</h2>
  <svg class="arrow" style="left:80px;top:224px" width="14" height="26"><path d="M12 1L2 13l10 12" fill="none" stroke="#333" stroke-width="2"/></svg>
  <svg class="arrow" style="left:1104px;top:224px" width="14" height="26"><path d="M2 1l10 12L2 25" fill="none" stroke="#333" stroke-width="2"/></svg>
  <article class="article" style="left:133px"><div class="photo" role="img" aria-label="Healthy bowls with vegetables, eggs and rice" style="background:linear-gradient(135deg,#2a3a3a,#c88a3a 50%,#6a8a3a)"></div>
    <div class="body"><time>27 Aug, 2020</time><h3>LOREM IPSUM IS SIMPLY DUMMY LOREM IPSUM.</h3><p>There are many variations of passages of Lorem Ipsum ava ilable, but the majority have suffered alteration.</p><span class="more">READ MORE</span></div></article>
  <article class="article" style="left:606px"><div class="photo" role="img" aria-label="Fresh greens, sprouts and pears on a table" style="background:linear-gradient(135deg,#5a8a2a,#3a4a2a 50%,#d8c8a8)"></div>
    <div class="body"><time>27 Aug, 2020</time><h3>LOREM IPSUM IS SIMPLY DUMMY LOREM IPSUM.</h3><p>There are many variations of passages of Lorem Ipsum ava ilable, but the majority have suffered alteration.</p><span class="more">READ MORE</span></div></article>
</section>

<footer class="site-footer">
  <div class="footer-brand">ZippyGrub</div>
  <div class="footer-col" style="left:503px"><h4>MENU</h4><ul><li>HOME</li><li>FOOD</li><li>RESTAURANTS</li><li>HOW IT WORKS</li><li>BLOG</li></ul></div>
  <div class="footer-col" style="left:690px"><h4>CONTACT US</h4>
    <div class="contact-item"><span class="dot"><svg width="8" height="11" viewBox="0 0 10 14"><path d="M5 0a5 5 0 0 0-5 5c0 4 5 9 5 9s5-5 5-9a5 5 0 0 0-5-5zm0 7a2 2 0 1 1 0-4 2 2 0 0 1 0 4z" fill="#333"/></svg></span><span>2210 Maple Row<br>Fairhill, CA 90000</span></div>
    <div class="contact-item"><span class="dot"><svg width="11" height="11" viewBox="0 0 12 12"><path d="M2 1l2.5 0 1 3-1.5 1a7 7 0 0 0 3 3l1-1.5 3 1V10a1.5 1.5 0 0 1-1.5 1.5C5 11.5.5 7 .5 2.5A1.5 1.5 0 0 1 2 1z" fill="#333"/></svg></span><span>Call Us<br>555.014.2277</span></div>
    <div class="contact-item"><span class="dot"><svg width="11" height="8" viewBox="0 0 12 9"><rect width="12" height="9" fill="#333"/><path d="M0 0l6 5 6-5" fill="none" stroke="#fff"/></svg></span><span>E mail Us<br>info@zippygrub.com</span></div>
  </div>
  <div class="footer-col" style="left:954px"><h4>FOLLOW US</h4>
    <div class="contact-item"><span class="dot"></span><span>Like us on<br>CIRCLEBOOK</span></div>
    <div class="contact-item"><span class="dot"></span><span>Follow us on<br>CHIRPLINE</span></div>
    <div class="contact-item"><span class="dot"></span><span>Follow us on<br>WORKNET</span></div>
  </div>
  <div class="footer-rule"></div>
  <div class="copyright">Copyright © 2020 All Rights Reserved</div>
</footer>

</body>
</html>
```